Business cards for start-up accounting firm

I'm looking for a double sided business card ready for upload into Lumo print or similar print providers with no modification required by me.
I'm looking for something simple as i think cards that are too 'busy' actually detract from the message. I have some thoughts but more than happy to see what comes up. The logo i have came out of left field and i love it the moment i saw it!

My thoughts:

Side 1: Just the logo, perhaps on a dark grey or charcoal background to make the logo colours stand out?

Side 2: The call to action from me website 'Looking for a more relaxed, friendly and interactive relationship with your accountant?' with my contact information
Name: Gus Tarrow
Email: gus@ledgerowl.com.au
Website: www.ledgerowl.com.au
Phone: 1300 762 349

The call to action needs to be the first thing they see when they look at side 2. If it helps to know what we do and how we do it there is a draft website at www.ledgerowl.com.au

Like i said, happy to consider anything that comes up :)

Target Market(s)

i'm targeting small business owners who experience a lot of stress around finacial reporting and have had bad experiences with accountants in the past.

Industry/Entity Type

Accounting

Contact Information for Business Card

Contained in the Description

Font styles to use
Serif
Sans Serif
Other font styles liked:
• See logo files attached

Colors
474747

Requirements
Must have
• My logo, slogan and contact information

```html
<!DOCTYPE html>
<html lang="en">
<head>
<meta charset="utf-8">
<title>Ledger Owl – Business Card</title>
<link rel="stylesheet" href="https://fonts.googleapis.com/css2?family=Open+Sans:wght@400;600;700&family=Tinos:ital@1&display=swap">
<style>
  :root {
    --charcoal: #343b3d;
    --yellow: #fad800;
    --purple: #7510b5;
    --white: #ffffff;
    --page: #ffffff;
  }
  * { margin: 0; padding: 0; box-sizing: border-box; }
  html, body {
    width: 1200px; height: 1000px; overflow: hidden;
    background: var(--page);
    font-family: "Open Sans", Arial, sans-serif;
  }
  .canvas { position: relative; width: 1200px; height: 1000px; }

  .card {
    position: absolute;
    width: 735px; height: 452px;
    background: var(--charcoal);
    overflow: hidden;
  }
  .card--front { left: 36px; top: 74px; }
  .card--back { left: 427px; top: 473px; }

  /* Front */
  .brand-name {
    color: var(--yellow);
    font-weight: 700;
    line-height: 1;
    white-space: nowrap;
  }
  .brand-name--large {
    position: absolute; left: 0; right: 0; top: 120px; height: 180px;
    display: flex; align-items: center; justify-content: center;
    font-size: 80px; letter-spacing: 1px;
  }

  /* Back */
  .accent-shapes { position: absolute; left: 0; top: 0; }
  .call-to-action {
    position: absolute; left: 170px; top: 99px;
    color: var(--white);
    font-family: "Tinos", "Times New Roman", serif;
    font-style: italic;
    font-size: 26px; line-height: 36px;
    letter-spacing: 1px;
    white-space: nowrap;
  }
  .brand-name--small {
    position: absolute; left: 168px; top: 247px;
    font-size: 26px; letter-spacing: 0.5px;
  }
  .contact-block { position: absolute; left: 169px; top: 302px; color: var(--white); }
  .contact-name {
    font-size: 19px; font-weight: 600; line-height: 26px; letter-spacing: 0.3px;
  }
  .contact-list { list-style: none; font-size: 18px; line-height: 26px; }
  .contact-list b { font-weight: 700; }
</style>
</head>
<body>
<main class="canvas">
  <section class="card card--front" aria-label="Business card front">
    <div class="brand-name brand-name--large">LEDGER OWL</div>
  </section>

  <section class="card card--back" aria-label="Business card back">
    <svg class="accent-shapes" width="735" height="452" viewBox="0 0 735 452" aria-hidden="true">
      <polygon points="0,0 171,0 0,312" fill="var(--yellow)"/>
      <polygon points="51,222 163,452 0,452 0,312" fill="var(--purple)"/>
    </svg>
    <p class="call-to-action">Looking for a more relaxed, friendly and<br>interactive relationship with your accountant?</p>
    <div class="brand-name brand-name--small">LEDGER OWL</div>
    <div class="contact-block">
      <p class="contact-name">GUS TARROW</p>
      <ul class="contact-list">
        <li><b>E:</b> gus@ledgerowl.com.au</li>
        <li><b>W:</b> www.ledgerowl.com.au</li>
        <li><b>P:</b> 1300 762 349</li>
      </ul>
    </div>
  </section>
</main>
</body>
</html>
```